I need a simple, classy and stylish business card. I would like it to have a black background with white writing. I would like you to use my logo you designed on the front with the word 'Imagery" used underneath it in the same font. On the back I was thinking of the website at the top 'tormavine.com' Then my social media accounts, Can you use the instagram, Facebook and twitter logo then my handles?
Please let me know what you think.
Regards Lars
Industry/Entity Type
Business
Requirements
Must have
- Website: www.tormavine.com
- Social media handles..
- Instagram: @Lars_Tormavine_Imagery
- Facebook: Lars Tormavine Imagery
- Twitter: @Lars_Tormavin
- Email: info@tormavin.com
- Phone: 0473 518 609

```html
<!DOCTYPE html>
<html lang="en">
<head>
<meta charset="utf-8">
<title>Lars Tormavine Imagery – Business Card</title>
<link rel="stylesheet" href="https://fonts.googleapis.com/css2?family=Questrial&display=swap">
<style>
  :root {
    --page-bg: #e9e6e2;
    --card-black: #0b0b0b;
    --card-white: #ffffff;
    --ink-light: #ffffff;
    --ink-dark: #111111;
    --ink-soft: #333333;
    --card-shadow: 0 14px 30px rgba(0,0,0,0.25);
  }
  * { box-sizing: border-box; margin: 0; padding: 0; }
  html, body {
    width: 1200px; height: 913px; overflow: hidden;
    background: var(--page-bg);
    font-family: "Questrial", "Century Gothic", sans-serif;
  }
  .stage { position: relative; width: 1200px; height: 913px; }
  .card {
    position: absolute; width: 560px; height: 320px;
    border-radius: 4px; box-shadow: var(--card-shadow);
  }

  /* Front */
  .card-front {
    left: 70px; top: 110px;
    background: linear-gradient(160deg, #1e1e1e 0%, var(--card-black) 55%);
    color: var(--ink-light);
  }
  .brand {
    position: absolute; left: 70px; top: 110px;
    display: flex; align-items: center; gap: 26px;
  }
  .brand-dot {
    width: 70px; height: 70px; border-radius: 50%;
    background: var(--ink-light); flex: none;
  }
  .brand-text { line-height: 1.05; }
  .brand-name { font-size: 42px; letter-spacing: 0.5px; }
  .brand-sub { font-size: 42px; letter-spacing: 0.5px; padding-left: 70px; }

  /* Back */
  .card-back {
    left: 570px; top: 480px;
    background: var(--card-white);
    color: var(--ink-dark);
  }
  .person {
    position: absolute; right: 30px; top: 30px; text-align: left;
  }
  .person-name { font-size: 22px; letter-spacing: 1px; }
  .person-role { font-size: 12px; color: var(--ink-soft); margin-top: 2px; }

  .contact-list {
    position: absolute; left: 30px; bottom: 30px;
    list-style: none; display: flex; flex-direction: column; gap: 7px;
  }
  .contact-item {
    display: flex; align-items: center; gap: 10px;
    font-size: 17px; letter-spacing: 0.3px;
  }
  .contact-icon { width: 22px; height: 22px; flex: none; }
</style>
</head>
<body>
<main class="stage">

  <section class="card card-front" aria-label="Card front">
    <div class="brand">
      <span class="brand-dot" aria-hidden="true"></span>
      <div class="brand-text">
        <p class="brand-name">Lars Tormavine</p>
        <p class="brand-sub">Imagery</p>
      </div>
    </div>
  </section>

  <section class="card card-back" aria-label="Card back">
    <div class="person">
      <p class="person-name">Ellis Harrow</p>
      <p class="person-role">Managing Director</p>
    </div>

    <ul class="contact-list">
      <li class="contact-item">
        <svg class="contact-icon" viewBox="0 0 22 22" aria-hidden="true">
          <circle cx="11" cy="11" r="11" fill="#111"/>
          <path d="M7.5 6 l2 0 l1 3 l-1.3 1 a7 7 0 0 0 3 3 l1-1.3 l3 1 l0 2 a1.5 1.5 0 0 1-1.5 1.3 a9 9 0 0 1-8.5-8.5 a1.5 1.5 0 0 1 1.3-1.5z" fill="#fff"/>
        </svg>
        <span>0473 518 609</span>
      </li>
      <li class="contact-item">
        <svg class="contact-icon" viewBox="0 0 22 22" aria-hidden="true">
          <circle cx="11" cy="11" r="11" fill="#111"/>
          <g fill="none" stroke="#fff" stroke-width="1.2">
            <circle cx="11" cy="11" r="6.5"/>
            <ellipse cx="11" cy="11" rx="3" ry="6.5"/>
            <line x1="4.5" y1="11" x2="17.5" y2="11"/>
          </g>
        </svg>
        <span>www.tormavine.com</span>
      </li>
      <li class="contact-item">
        <svg class="contact-icon" viewBox="0 0 22 22" aria-hidden="true"><circle cx="11" cy="11" r="11" fill="#111"/></svg>
        <span>@Lars_Tormavine_Imagery</span>
      </li>
      <li class="contact-item">
        <svg class="contact-icon" viewBox="0 0 22 22" aria-hidden="true"><circle cx="11" cy="11" r="11" fill="#111"/></svg>
        <span>@LarsTormavineImagery</span>
      </li>
      <li class="contact-item">
        <svg class="contact-icon" viewBox="0 0 22 22" aria-hidden="true"><circle cx="11" cy="11" r="11" fill="#111"/></svg>
        <span>@Lars_Tormavin</span>
      </li>
    </ul>
  </section>

</main>
</body>
</html>
```